Process Engineering/Construction Firm wants a OneSheet targeting craft brewers in Texas

We need a OneSheet (standard letter size) that we can share with craft brewers in our state, that explains what we can do for them. This will be shared primarily via email and online. We would like to see this be fun and modern flyer while still maintaining our professional vibe. More info and logos are uploaded - please review. Also, this project could lead to more branded documents from OneSheets to letterhead. We have our website and our logo(s) and really not much else that is consistent. There is certainly opportunity to work long-term.
Updates

Please note that the website listed on the flyer should read www.halvernworksadvisory.com. It will NOT follow the same domain name as the email address. And also, please DO NOT send me anything through the sales@hwaadvisoryllc.com email address at this time. I am trying to find a brewery-specific photo to use and will upload once found. I will be uploading shortly another logo of an affiliate organization we belong to - the Lone Kettle Brewing Alliance that I would like to see included on the flyer with the words, "A proud member of the Lone Kettle Brewing Alliance' OR just 'Proud Member.'

Target Market(s)

Craft brewery owners in Texas

Industry/Entity Type

Engineering

Font styles to use
Sans Serif

Requirements
Must have
• We need our point of contact to list the website as well as this email: sales@hwaadvisoryllc.com
• Maroon CMYK is: 32, 100, 82, 30
• We want these Brewery Specific service points included:
• • Brewhouse automation
• • Glycol systems
• • Complete line design and install
• • Packaging solutions
• • Epoxy & urethane flooring
• • New construction
• • Network of industry professionals
Nice to have
• Trendy and modern look to correlate with current craft beer logos and design trends

```html
<!DOCTYPE html>
<html lang="en">
<head>
<meta charset="utf-8">
<title>Halvern Works – Precision engineering and construction solutions</title>
<link rel="stylesheet" href="https://fonts.googleapis.com/css2?family=Arvo:wght@700&family=Mulish:wght@400;600;800&display=swap">
<style>
  :root {
    --maroon: #8b1a32;
    --maroon-deep: #7a1429;
    --maroon-bright: #a62a52;
    --pink: #e0457c;
    --orange: #f6a532;
    --white: #ffffff;
  }
  * { margin: 0; padding: 0; box-sizing: border-box; }
  html, body { width: 927px; height: 1200px; overflow: hidden; background: var(--maroon); }
  .sheet {
    position: relative;
    width: 927px;
    height: 1200px;
    overflow: hidden;
    background:
      repeating-linear-gradient(115deg, rgba(255,255,255,0) 0 90px, rgba(255,255,255,0.045) 90px 170px),
      linear-gradient(100deg, var(--maroon-deep) 0%, var(--maroon) 45%, var(--maroon-bright) 100%);
    font-family: 'Mulish', sans-serif;
    color: var(--white);
  }
  .site-photo {
    position: absolute;
    left: 0; top: 195px;
    width: 927px; height: 300px;
    background:
      linear-gradient(90deg, rgba(120,30,50,0.25) 0%, rgba(215,80,115,0.25) 60%, rgba(200,70,100,0.15) 100%),
      linear-gradient(180deg, rgba(200,70,100,0) 0%, rgba(205,75,105,0.35) 40%, rgba(190,60,90,0.45) 80%, rgba(180,50,80,0) 100%);
  }
  .art { position: absolute; inset: 0; width: 927px; height: 1200px; }
  .brand-box {
    position: absolute;
    left: 70px; top: 0;
    width: 254px; height: 185px;
    background: var(--white);
    display: flex;
    align-items: center;
    justify-content: center;
  }
  .brand-name {
    font-family: 'Arvo', serif;
    font-weight: 700;
    font-size: 34px;
    line-height: 1.05;
    color: var(--maroon);
    text-align: center;
  }
  .contact { position: absolute; right: 77px; top: 60px; text-align: right; }
  .contact-phone {
    font-weight: 800;
    font-size: 52px;
    letter-spacing: 0.5px;
    color: var(--orange);
    line-height: 1;
  }
  .contact-email {
    margin-top: 20px;
    font-size: 25px;
    letter-spacing: 0.6px;
    line-height: 1;
  }
  .headline {
    position: absolute;
    left: 70px; top: 218px;
    font-family: 'Arvo', serif;
    font-weight: 700;
    font-size: 47px;
    line-height: 52px;
    letter-spacing: 0.3px;
  }
  .membership {
    position: absolute;
    right: 40px; top: 282px;
    display: flex;
    align-items: center;
    gap: 10px;
    font-weight: 600;
    font-size: 14px;
    line-height: 18px;
    letter-spacing: 0.3px;
  }
  .membership-badge {
    width: 38px; height: 38px;
    border-radius: 50%;
    border: 2px solid var(--orange);
    flex: none;
  }
  .services {
    position: absolute;
    left: 70px; top: 346px;
    list-style: none;
    font-size: 26px;
    letter-spacing: 1.6px;
    line-height: 35.4px;
  }
  .services li { position: relative; padding-left: 30px; }
  .services li::before {
    content: "";
    position: absolute;
    left: 4px; top: 15px;
    width: 7px; height: 7px;
    border-radius: 50%;
    background: var(--white);
  }
  .website {
    position: absolute;
    left: 0; right: 0; top: 1134px;
    text-align: center;
    font-size: 26px;
    letter-spacing: 0.6px;
    padding-left: 10px;
    text-shadow: 0 1px 3px rgba(0,0,0,0.45);
  }
</style>
</head>
<body>
<main class="sheet">
  <div class="site-photo" role="img" aria-label="Faded photo of a brewery construction site with drilling rigs and rebar"></div>

  <svg class="art" viewBox="0 0 927 1200">
    <defs>
      <linearGradient id="facility-h" x1="0" y1="0" x2="1" y2="0">
        <stop offset="0" stop-color="#9ea3a6"/>
        <stop offset="0.35" stop-color="#c7c9c6"/>
        <stop offset="0.7" stop-color="#8e9194"/>
        <stop offset="1" stop-color="#6d7073"/>
      </linearGradient>
      <linearGradient id="facility-v" x1="0" y1="0" x2="0" y2="1">
        <stop offset="0" stop-color="#5e6264" stop-opacity="0.5"/>
        <stop offset="0.55" stop-color="#ffffff" stop-opacity="0"/>
        <stop offset="0.8" stop-color="#c9b23a" stop-opacity="0.25"/>
        <stop offset="1" stop-color="#4a4a48" stop-opacity="0.6"/>
      </linearGradient>
      <linearGradient id="tank-h" x1="0" y1="0" x2="1" y2="0">
        <stop offset="0" stop-color="#344a2a"/>
        <stop offset="0.35" stop-color="#55603f"/>
        <stop offset="0.6" stop-color="#bda985"/>
        <stop offset="1" stop-color="#d6c3a0"/>
      </linearGradient>
      <linearGradient id="tank-v" x1="0" y1="0" x2="0" y2="1">
        <stop offset="0" stop-color="#dfe3e0" stop-opacity="0.35"/>
        <stop offset="0.5" stop-color="#ffffff" stop-opacity="0"/>
        <stop offset="0.85" stop-color="#a69a84" stop-opacity="0.35"/>
        <stop offset="1" stop-color="#8a8476" stop-opacity="0.5"/>
      </linearGradient>
      <linearGradient id="line-h" x1="0" y1="0" x2="1" y2="0">
        <stop offset="0" stop-color="#7a2a2e"/>
        <stop offset="0.2" stop-color="#a9a8a2"/>
        <stop offset="0.55" stop-color="#c8323e"/>
        <stop offset="0.75" stop-color="#b52a36"/>
        <stop offset="1" stop-color="#c4c6c2"/>
      </linearGradient>
    </defs>
    <g role="img" aria-label="Photo of a brewery interior with a glass-walled room, stop sign and yellow safety bollards">
      <polygon points="0,844 385,664 385,1200 0,1200" fill="url(#facility-h)"/>
      <polygon points="0,844 385,664 385,1200 0,1200" fill="url(#facility-v)"/>
    </g>
    <g role="img" aria-label="Photo of a tan water storage tank with a caged ladder, trees and fence">
      <polygon points="387,663 927,411 927,952 387,952" fill="url(#tank-h)"/>
      <polygon points="387,663 927,411 927,952 387,952" fill="url(#tank-v)"/>
    </g>
    <rect x="387" y="954" width="540" height="246" fill="url(#line-h)" role="img" aria-label="Photo of a packaging line conveyor full of red cans"/>
    <polygon points="0,830 927,397 927,413 0,846" fill="var(--pink)"/>
    <polygon points="0,827 927,394 927,398 0,831" fill="var(--orange)"/>
  </svg>

  <header class="brand-box">
    <div class="brand-name">Halvern<br>Works</div>
  </header>

  <div class="contact">
    <div class="contact-phone">254-555-0186</div>
    <div class="contact-email">sales@hwaadvisoryllc.com</div>
  </div>

  <h1 class="headline">Precision engineering and<br>construction solutions</h1>

  <div class="membership">
    <span class="membership-badge" role="img" aria-label="Alliance member badge"></span>
    <span>A proud member of the<br>Lone Kettle Brewing Alliance</span>
  </div>

  <ul class="services">
    <li>Brewhouse automation</li>
    <li>Glycol systems</li>
    <li>Complete line design and install</li>
    <li>Packaging solutions</li>
    <li>Epoxy &amp; urethane flooring</li>
    <li>New construction</li>
    <li>Network of industry<br>professionals</li>
  </ul>

  <footer class="website">www.halvernworksadvisory.com</footer>
</main>
</body>
</html>
```